Homepage mockup for PivotMarkScore.com

I would like a homepage mockup of pivotmarkscore.com.

Basically what the site does, is it allows a person to upload a video of a gymnastics routine and our certified judges will judge the routine providing a score, as well as provide a critique and feedback as to why they gave you that score. Many times people don't know why they got the score they did at a gymnastics competition, so this site aims to provide reasoning behind it.

I have started to design the homepage myself (see attached), and like it, but I'd like a professional to finish the layout, or even come up with something really wow and original. I like clean, typically simple design.

THIS IS AN OLD VERSION OF THE SITE (http://esite.krelnavo.com/) This should only be used so you can get an idea of what the site is about. I DO NOT want the new site to look like this, but the basic concept and content remains the same.

DESIGNER FILES CAN BE DOWNLOADED HERE (http://krelnavo.com/files.aspx)

Target Market(s)

Gymnastic type people, parents of gymnasts, coaches, etc.

Industry/Entity Type

It Professional

Requirements
Must have
• -The pivot mark logo (provided)
-Not required, but I have attached the main photo I used in my mockup (AI File)
*A step by step graphic(s) depicting the process for a user. A How it works sort of explanation. Should be eye catching, not just text.

-Step 1: Videotape your gymnastic routine.
-Step 2: Create an account and share us your video.
-Step 3: Our certified judges will score and critique your routine, fully explaining the reasons behind their score.

```html
<!DOCTYPE html>
<html lang="en">
<head>
<meta charset="utf-8">
<title>The Pivot Mark — Home</title>
<link href="https://fonts.googleapis.com/css2?family=Play:wght@400;700&family=Roboto:wght@300;400&display=swap" rel="stylesheet">
<style>
:root{
  --paper:#f1f1f1;
  --hero-top:#e9e9e9;
  --hero-bottom:#fbfbfb;
  --blue:#1f5fc6;
  --blue-dark:#1848a0;
  --blue-soft:#3f77d6;
  --red:#e03a26;
  --red-dark:#b72a1f;
  --grey-band:#ebebeb;
  --text-dark:#111;
  --text-grey:#6b6b6b;
  --pill:#f4f2ee;
  --pill-text:#555;
  --footer:#000;
  --floor:#d9c7ab;
}
*{box-sizing:border-box;margin:0;padding:0}
html,body{width:1200px;height:1052px;overflow:hidden}
body{position:relative;background:var(--paper);font-family:'Roboto',Arial,sans-serif}
.site-header{position:absolute;left:0;top:0;width:1200px;height:133px;background:var(--paper)}
.brand{position:absolute;left:150px;top:50px;display:flex;align-items:center;gap:10px;font-family:'Play',sans-serif;font-weight:700;font-size:38px;color:var(--blue);line-height:1}
.brand-dot{width:14px;height:14px;border-radius:50%;background:var(--red)}
.login{position:absolute;top:69px;left:625px;display:flex;gap:13px;align-items:center}
.field{height:35px;border-radius:18px;background:#fff;border:1px solid #d6d6d6;display:flex;align-items:center;padding-left:14px;gap:9px;font-size:13px;color:#8a8a8a;text-transform:uppercase;letter-spacing:.2px}
.field.email{width:162px}.field.pass{width:162px}
.btn-login{width:80px;height:34px;border-radius:17px;background:linear-gradient(var(--red),var(--red-dark));color:#fff;font-size:16px;display:flex;align-items:center;justify-content:center;border:2px solid #f0f0f0}
.nav-band{position:absolute;left:0;top:133px;width:1200px;height:17px;background:var(--blue)}
.nav-bar{position:absolute;left:118px;top:133px;width:962px;height:50px;background:var(--blue);border-radius:0 0 28px 28px}
.nav{position:absolute;top:145px;left:147px;display:flex;gap:9px}
.nav a{height:28px;border-radius:14px;background:var(--pill);color:var(--pill-text);font-size:13.5px;text-decoration:none;display:flex;align-items:center;justify-content:center;box-shadow:inset 0 -2px 3px rgba(0,0,0,.12)}
.search{position:absolute;left:878px;top:145px;width:170px;height:26px;border-radius:13px;background:#fff;font-family:Georgia,serif;font-size:12px;color:#777;padding-left:18px;display:flex;align-items:center}
.search svg{position:absolute;right:14px;top:6px}
.hero{position:absolute;left:0;top:183px;width:1200px;height:392px;background:linear-gradient(var(--hero-top),var(--hero-bottom))}
.floor{position:absolute;left:0;top:545px;width:1200px;height:30px;background:linear-gradient(#e8dcc8,var(--floor))}
.photo{position:absolute;left:470px;top:230px;width:340px;height:340px;background:radial-gradient(ellipse at 45% 55%,#8a7c72 0%,#b9b0a8 35%,rgba(240,240,240,0) 70%)}
.score-cards{position:absolute;left:632px;top:318px;width:140px;height:110px;background:radial-gradient(#f3eee3 40%,rgba(243,238,227,0) 72%)}
.steps{position:absolute;left:140px;top:265px;list-style:none}
.steps li{position:relative;width:303px;height:63px;margin-bottom:8px;background:linear-gradient(90deg,var(--red),var(--red-dark));font-family:'Play',sans-serif;font-size:21px;color:#fff;padding-left:69px;display:flex;align-items:center}
.steps li span{position:absolute;left:0;top:4px;width:56px;height:56px;border-radius:50%;background:var(--blue-soft);border:3px solid #fff;box-shadow:0 0 0 1px #ddd;display:flex;align-items:center;justify-content:center;font-size:25px;font-family:'Roboto',sans-serif;font-weight:300}
.tagline{position:absolute;left:794px;top:296px;font-family:'Play',sans-serif;font-size:21px;line-height:24px;color:var(--text-dark)}
.why-mark{position:absolute;left:1012px;top:360px;width:48px;height:24px;border-radius:4px;background:rgba(31,95,198,.15)}
.cta{position:absolute;left:794px;top:390px;width:259px;height:67px;border-radius:22px;background:#a9a9a9;padding:8px}
.cta-inner{width:100%;height:100%;border-radius:16px;background:linear-gradient(var(--blue-soft),var(--blue-dark));display:flex;align-items:center;color:#fff;padding-left:12px}
.cta small{font-size:11.5px;line-height:12px;text-align:right;font-weight:400;width:114px}
.cta strong{font-family:'Play',sans-serif;font-size:22px;margin-left:14px}
.process{position:absolute;left:0;top:575px;width:1200px;height:422px;background:var(--grey-band)}
.process svg{position:absolute;left:0;top:0}
.label{position:absolute;font-size:20px;font-weight:300;color:var(--text-grey);line-height:24px}
.site-footer{position:absolute;left:0;top:997px;width:1200px;height:55px;background:var(--footer);color:#fff;font-size:12px}
.foot-nav{position:absolute;left:151px;top:21px;display:flex;gap:20px}
.copy{position:absolute;right:151px;top:21px}
</style>
</head>
<body>
<header class="site-header">
  <div class="brand"><span>The Pivot Mark</span><span class="brand-dot"></span></div>
  <div class="login">
    <div class="field email"><svg width="15" height="11"><rect x=".5" y=".5" width="14" height="10" fill="#666"/><path d="M1 1l6.5 5L14 1" stroke="#fff" fill="none"/></svg>Email adress</div>
    <div class="field pass"><svg width="12" height="12"><circle cx="6" cy="3.5" r="3" fill="#666"/><path d="M0 12a6 5 0 0 1 12 0z" fill="#666"/></svg>Password</div>
    <div class="btn-login">LOGIN</div>
  </div>
</header>
<div class="nav-band"></div>
<div class="nav-bar"></div>
<nav class="nav">
  <a style="width:111px">How it Works</a>
  <a style="width:111px">Faq</a>
  <a style="width:117px">Sample critique</a>
  <a style="width:112px">Member Area</a>
  <a style="width:112px">About</a>
</nav>
<div class="search">search<svg width="14" height="14"><circle cx="5.5" cy="5.5" r="4" stroke="var(--blue)" stroke-width="2" fill="none"/><path d="M8.5 8.5l4 4" stroke="var(--blue)" stroke-width="2.5"/></svg></div>

<section class="hero">
</section>
<div class="floor"></div>
<div class="photo" role="img" aria-label="Photo of a gymnast in a black leotard holding a split handstand on the beam"></div>
<div class="score-cards" role="img" aria-label="Illustration of judging score cards pinned with red pins"></div>
<ol class="steps">
  <li><span>1</span>Record Your Routine</li>
  <li><span>2</span>Sign Up And Upload</li>
  <li><span>3</span>Get The “Why”</li>
</ol>
<p class="tagline">Judges will give you marks<br>we will explain the reason...</p>
<div class="why-mark" role="img" aria-label="Hand lettered word Why"></div>
<div class="cta"><div class="cta-inner"><small>Upload your video<br>&amp; get critiqued!</small><strong>Get started</strong></div></div>

<section class="process">
  <svg width="1200" height="422" viewBox="0 575 1200 422">
    <g fill="none" stroke-width="1.4">
      <path d="M197 656H331V740" stroke="var(--blue)"/>
      <path d="M422 786L552 746" stroke="var(--blue)"/>
      <path d="M725 772L884 815" stroke="var(--red)"/>
      <path d="M647 828V907H512" stroke="var(--red)"/>
      <path d="M830 682H963V762" stroke="#666"/>
    </g>
    <!-- reel step -->
    <path d="M300 880A72 72 0 0 0 410 760A78 78 0 0 1 300 890Z" fill="var(--blue)" opacity=".85"/>
    <circle cx="335" cy="815" r="71" fill="#fff" stroke="#ddd"/>
    <circle cx="330" cy="810" r="38" fill="#c9c9c9" stroke="#555" stroke-width="3"/>
    <g fill="#444"><circle cx="330" cy="790" r="8"/><circle cx="330" cy="830" r="8"/><circle cx="310" cy="810" r="8"/><circle cx="350" cy="810" r="8"/><circle cx="330" cy="810" r="4"/></g>
    <path d="M300 850Q340 868 385 840L392 852Q340 882 296 862Z" fill="#222"/>
    <!-- judge step -->
    <path d="M610 815A75 75 0 0 1 650 668A70 70 0 0 0 610 815Z" fill="var(--red)"/>
    <circle cx="647" cy="745" r="68" fill="#fff" stroke="#ddd"/>
    <rect x="607" y="700" width="68" height="82" fill="#f0801e"/>
    <g stroke="#fff" stroke-width="3"><path d="M616 715H666M616 727H640M616 739H640M616 751H640M616 763H640"/></g>
    <path d="M636 745H668V728L695 765L668 795V780H636Z" fill="var(--blue)"/>
    <!-- result step -->
    <path d="M990 780A75 75 0 0 1 960 930A80 80 0 0 0 990 780Z" fill="#777"/>
    <circle cx="968" cy="853" r="72" fill="#fff" stroke="#ddd"/>
    <path d="M932 813H992L1006 827V903H932Z" fill="#eee" stroke="#bbb"/>
    <path d="M962 840H990V826L1018 853L990 880V866H962Z" fill="var(--blue)"/>
    <!-- badges -->
    <g font-family="Roboto,sans-serif" font-size="20" fill="#fff" text-anchor="middle">
      <circle cx="173" cy="656" r="22" fill="#fff" stroke="var(--blue)" stroke-width="3"/>
      <circle cx="175" cy="656" r="17" fill="var(--blue)"/><text x="175" y="663">1</text>
      <circle cx="488" cy="908" r="22" fill="#fff" stroke="var(--red)" stroke-width="3"/>
      <circle cx="490" cy="908" r="17" fill="var(--red)"/><text x="490" y="915">2</text>
      <circle cx="803" cy="683" r="22" fill="#fff" stroke="#666" stroke-width="3"/>
      <circle cx="805" cy="683" r="17" fill="#5d5353"/><text x="805" y="690">3</text>
    </g>
  </svg>
  <p class="label" style="left:206px;top:30px">Upload your Video</p>
  <p class="label" style="left:824px;top:30px">Get the “Why” and<br>much more</p>
  <p class="label" style="left:530px;top:355px">We’ll Judge your Routine</p>
</section>

<footer class="site-footer">
  <nav class="foot-nav"><span>How It Works</span><span>Faq</span><span>Sample Critique</span><span>Member Area</span><span>About</span></nav>
  <p class="copy">©copyright2012 The Pivot Mark. All Rights Reserved</p>
</footer>
</body>
</html>
```